Packaging Artwork for "Earth's First Expanding Biodisposable Loofah Pads"

Our company manufactures BrisaPods. They are Earth's first expanding, biodisposable loofah pads for exfoliating the skin.
BrisaPods are biodisposable, so they can be thrown-away (or composted) before nasty skin bacteria can grow on them. This makes scrubbing skin cleaner and safer.
This is a high-end product, so our packaging needs to be very clean, sophisticated and make our product look like it should be expensive. The packaging should also let the viewer know the product is environmentally friendly.
The product name is "BrisaPods". The packaging also has to say "Biodisposable".
Our new packaging is a hanging bag with a window in it. See the image attached. There is also a picture of our current packaging for our Tarnivelles sponges. We would like completely different artwork, but keep the white paper.
The attached images are of our kitchen cleaning pads "Quorlimates". This new packaging is for "BrisaPods" which are a beauty product and the artwork must be different. Also, the packaging should have a large image of the round loofah pad on the front and the image of the loofah expanding from thin to thick on the back.
Updates

This will be a 4-inch x 4-inch bag that will hang from a hook. The bag will be about 2-inches thick. The logo will be similar to the Quorlimates fish logo that has been added to the project. Instead of saying "tarnivelles", the word "BrisaPods" needs to be used in the logo.

Industry/Entity Type

health and beauty

Requirements
Must have
• slogan "Clean Germ Free. Guilt Free". The product should be called "Earth's First Expanding Biodisposable Bath Loofahs". simple clean design on a white background. see the picture of our current packaging below. We will use the same paper. We just need completely different, sophisticated artwork

```html
<!DOCTYPE html>
<html lang="en">
<head>
<meta charset="utf-8">
<title>BrisaPods – Packaging Artwork</title>
<link rel="stylesheet" href="https://fonts.googleapis.com/css2?family=Source+Sans+3:wght@400;600&family=Roboto:wght@400;500&display=swap">
<style>
  :root {
    --backdrop: #d6d6d6;
    --ink: #3d3a3b;
    --brand: #5b4a4c;
    --gold: #e8bc5e;
    --paper: #ffffff;
    --teal: #66a9a8;
    --teal-light: #8fd3d9;
    --tag: #6b5457;
    --icon: #4f5f61;
    --label: #f2f8f8;
  }
  * { margin: 0; padding: 0; box-sizing: border-box; }
  html, body {
    width: 1200px; height: 1200px; overflow: hidden;
    background: var(--backdrop);
  }
  .artwork { position: relative; width: 1200px; height: 1200px; }

  .corner-flag { position: absolute; left: 714px; top: 669px; }

  .headline {
    position: absolute; left: 169px; width: 846px; top: 700px;
    text-align: center;
    font-family: "Source Sans 3", sans-serif;
    font-weight: 400; font-size: 31px; line-height: 37px;
    color: var(--ink);
  }

  .paper-band {
    position: absolute; left: 169px; top: 790px; width: 846px; height: 149px;
    background: var(--paper);
  }
  .side-copy {
    position: absolute; left: 29px; top: 18px; width: 150px;
    font-family: "Roboto", sans-serif; font-weight: 500;
    font-size: 6.6px; line-height: 8.8px; color: #3b3435;
  }
  .side-copy p + p { margin-top: 8px; }

  .wordmark {
    position: absolute; left: 290px; top: 44px;
    display: flex; align-items: center; gap: 12px;
  }
  .wordmark-dot {
    width: 44px; height: 44px; border-radius: 50%;
    background: var(--teal);
  }
  .wordmark-name {
    font-family: "Source Sans 3", sans-serif; font-weight: 400;
    font-size: 46px; line-height: 1; color: var(--brand);
  }

  .slogan-tag {
    position: absolute; left: 495px; top: 961px; width: 177px; height: 16px;
    background: var(--tag); border-radius: 2px 2px 0 0;
    display: flex; align-items: center; justify-content: center; gap: 14px;
    font-family: "Source Sans 3", sans-serif; font-size: 11px;
    color: #f3eeee;
  }

  .teal-band {
    position: absolute; left: 169px; top: 977px; width: 846px; height: 115px;
    background: var(--teal);
  }
  .benefit {
    position: absolute; top: 10px; width: 140px; text-align: center;
    font-family: "Roboto", sans-serif; font-size: 14px; color: var(--label);
  }
  .benefit svg { display: block; margin: 0 auto 6px; }
  .benefit--plants { left: 203px; }
  .benefit--tough { left: 347px; }
  .benefit--bio { left: 486px; }
  .fine-print {
    position: absolute; left: 667px; top: 40px; width: 150px;
    font-family: "Roboto", sans-serif; font-size: 5.4px; line-height: 8.6px;
    color: var(--label);
  }
</style>
</head>
<body>
<main class="artwork">
  <svg class="corner-flag" width="89" height="77" viewBox="0 0 89 77" aria-hidden="true">
    <polygon points="0,0 89,0 89,77" fill="var(--gold)"/>
  </svg>

  <h1 class="headline">Earth's First Expanding<br>Biodisposable Loofah Pads</h1>

  <section class="paper-band">
    <div class="side-copy">
      <p>Lorem ipsum dolor sit amet, consectetur adipiscing elit, sed do eiusmod tempor incididunt ut labore et dolore magna aliqua. Quis ipsum suspendisse ultrices gravida. Risus commodo viverra maecenas accumsan lacus vel facilisis.</p>
      <p>Lorem ipsum dolor sit amet, consectetur adipiscing elit, sed do eiusmod tempor incididunt ut labore et dolore magna aliqua. Quis ipsum suspendisse ultrices gravida. Risus commodo viverra maecenas accumsan</p>
    </div>
    <div class="wordmark">
      <span class="wordmark-dot"></span>
      <span class="wordmark-name">BrisaPods™</span>
    </div>
  </section>

  <div class="slogan-tag">
    <span>Germ Free</span>
    <svg width="11" height="10" viewBox="0 0 24 22" aria-hidden="true"><path d="M12 21 C4 15 0 11 0 6 A6 6 0 0 1 12 4 A6 6 0 0 1 24 6 C24 11 20 15 12 21Z" fill="var(--teal-light)"/></svg>
    <span>Guilt Free</span>
  </div>

  <section class="teal-band">
    <div class="benefit benefit--plants">
      <svg width="52" height="56" viewBox="0 0 52 56" fill="none" stroke="var(--icon)" stroke-width="2.4" stroke-linecap="round" stroke-linejoin="round" aria-hidden="true">
        <path d="M48 3 C30 4 14 10 11 26 C9 38 20 44 32 36 C44 28 46 14 48 3Z"/>
        <path d="M40 12 C28 22 16 36 4 54"/>
      </svg>
      All Plants
    </div>
    <div class="benefit benefit--tough">
      <svg width="56" height="56" viewBox="0 0 56 56" fill="none" stroke="var(--icon)" stroke-width="2.4" stroke-linecap="round" stroke-linejoin="round" aria-hidden="true">
        <path d="M8 22 A21 21 0 0 1 46 14"/><path d="M40 15 L47 15 L47 8"/>
        <path d="M48 34 A21 21 0 0 1 10 42"/><path d="M16 41 L9 41 L9 48"/>
        <path d="M31 15 L22 30 L29 30 L25 41 L34 26 L27 26 Z"/>
      </svg>
      Tough
    </div>
    <div class="benefit benefit--bio">
      <svg width="56" height="56" viewBox="0 0 56 56" fill="none" stroke="var(--icon)" stroke-width="2.4" stroke-linecap="round" stroke-linejoin="round" aria-hidden="true">
        <path d="M8 22 A21 21 0 0 1 46 14"/><path d="M40 15 L47 15 L47 8"/>
        <path d="M48 34 A21 21 0 0 1 10 42"/><path d="M16 41 L9 41 L9 48"/>
        <path d="M28 14 C22 22 19 27 19 31 A9 9 0 0 0 37 31 C37 27 34 22 28 14Z"/>
        <path d="M25 32 A3 3 0 0 0 28 35"/>
      </svg>
      Biodegradable
    </div>
    <p class="fine-print">Lorem ipsum dolor sit amet, consectetur adipiscing elit, sed do eiusmod tempor incididunt ut labore et dolore magna aliqua. Quis ipsum suspendisse ultrices gravida. Risus commodo viverra maecenas accumsan lacus vel facilisis.</p>
  </section>
</main>
</body>
</html>
```